Bright Harbor Capital website

Build a website template for the Bright Harbor Capital fund.
Looking for a cool website design showing companies we are using the latest in web design trends. We want to attract app developers, typically the younger set.
A good example of one of our competitive firms is http://mossfinch.org
The required components for the website include:
1) Funding application
2) about our firm
a) Partner profiles - We will include photographs and bios about each of the partners in our firm.
b) Invest with Bright Harbor - This will include information how to invest with our fund
c) our process - About our process for evaluating, funding and helping build successful businesses - This will include a narrative about the target companies, how we work, the type of deals we are interested in, our expectations, etc ...
3) Investment profiles - Stories about the companies we invest with
4) News - Output from our twitter feed and copies of our Blog posts

```html
<!DOCTYPE html>
<html lang="en">
<head>
<meta charset="utf-8">
<title>Bright Harbor Capital</title>
<link href="https://fonts.googleapis.com/css2?family=Lato:ital,wght@0,400;0,700;0,900;1,400&display=swap" rel="stylesheet">
<style>
:root{
  --green:#5a9a16;
  --green-light:#7cb43a;
  --text:#222;
  --muted:#666;
  --line:#dcdcdc;
  --page:#efefef;
  --white:#fff;
}
*{box-sizing:border-box;margin:0;padding:0}
html,body{width:1200px;height:910px;overflow:hidden}
body{position:relative;background:var(--page);font-family:'Lato',sans-serif;color:var(--text)}
a{text-decoration:none;color:inherit}
.abs{position:absolute}
.topbar{left:0;top:0;width:1200px;height:22px;background:var(--green)}
.toplinks{right:250px;top:5px;font-size:8px;color:#fff;display:flex;gap:8px;text-transform:uppercase}
.toplinks a{color:#fff}
.toplinks a.active{text-decoration:underline}
.header{left:0;top:22px;width:1200px;height:156px;background:linear-gradient(#f2f2f2,#d9d9d9)}
.brand-mark{left:332px;top:52px;width:30px;height:30px;border-radius:50%;background:var(--green)}
.brand{left:250px;top:92px;width:194px;text-align:center;color:var(--green);font-weight:700;font-size:24px;line-height:26px}
.nav{left:477px;top:121px;display:flex;gap:10px;font-size:11px;color:#777;align-items:center}
.nav span{padding:2px 3px}
.nav .current{background:#fff;border:1px solid #ccc;color:var(--green);text-decoration:underline}
.hero{left:475px;top:162px;width:475px;height:239px;border:1px solid #ccc;background:#ddd}
.hero-photo{width:100%;height:180px;background:linear-gradient(160deg,#c9d6df,#8e9aa5 55%,#b9a69a)}
.hero-caption{padding:10px 14px;font-size:8.5px;line-height:13px;color:#333;background:linear-gradient(#e0e0e0,#d3d3d3);height:59px}
.funding{left:250px;top:210px;width:194px;height:140px;background:linear-gradient(160deg,var(--green) 60%,var(--green-light) 60%);border:1px solid #4d8a12;text-align:center;text-decoration:none}
.funding h2{font-size:30px;font-weight:900;color:#fff;margin-top:22px;line-height:30px;letter-spacing:.5px}
.funding h3{font-size:21px;font-weight:700;color:#2a2a2a;line-height:22px}
.funding .go{display:block;margin:10px auto 0}
.panel{background:var(--white);border:1px solid var(--line)}
.panel-head{position:relative;background:var(--green);color:#fff;font-size:13px;height:30px;line-height:30px;padding-left:14px;text-transform:uppercase}
.panel-head svg{position:absolute;left:10px;top:30px}
.profiles{left:250px;top:381px;width:194px;height:230px}
.partner{text-align:center;color:#1c3c7a;font-size:15px;font-weight:700;margin-top:26px}
.partner + .partner{margin-top:22px}
.view-all{position:absolute;right:13px;font-size:10px;color:var(--green);text-decoration:underline}
.rule{left:475px;top:416px;width:475px;height:1px;background:#ccc}
.about{left:475px;top:430px;width:475px;height:180px;padding:12px 14px}
h4{color:var(--green);font-size:13px;font-weight:400;text-transform:uppercase}
.about ul{list-style:none;font-size:13px;line-height:17px}
.about li{position:relative;padding-left:10px}
.about li::before{content:"•";position:absolute;left:0}
.news{left:250px;top:638px;width:194px;height:194px}
.news-list{list-style:none;padding:10px 0 0 17px}
.news-list li{position:relative;padding-left:9px;margin-bottom:14px;font-size:9.5px;line-height:15px}
.news-list li::before{content:"";position:absolute;left:0;top:6px;width:3px;height:3px;border-radius:50%;background:var(--green)}
.news-list .date{color:var(--green)}
.growing{left:475px;top:638px;width:213px;height:194px;padding:14px 13px}
.growing p{font-size:13px;line-height:17px}
.quote{left:726px;top:638px;width:224px;height:194px;padding:14px 26px 14px 13px;font-style:italic;font-size:13px;line-height:17px}
.footer{left:0;top:870px;width:1200px;height:40px;background:var(--green);color:#fff;font-size:9px;font-family:Arial,sans-serif}
.footer p{position:absolute;left:250px;top:12px}
</style>
</head>
<body>
<div class="abs topbar"></div>
<div class="abs toplinks"><a class="active" href="#">Members</a><a href="#">Sponsors</a><a href="#">Latest News</a></div>
<div class="abs header"></div>

<svg class="abs" style="left:250px;top:22px" width="194" height="16" viewBox="0 0 194 16"><polygon points="0,0 194,0 194,4 97,16 0,4" fill="#5a9a16"/></svg>
<svg class="abs" style="left:250px;top:174px" width="194" height="22" viewBox="0 0 194 22"><polygon points="0,0 194,0 194,10 97,22 0,10" fill="#5a9a16"/></svg>

<div class="abs brand-mark"></div>
<div class="abs brand">Bright Harbor<br>Capital</div>

<nav class="abs nav"><span class="current">Home</span><span>About us</span><span>Partners profile</span><span>Invest</span><span>Our process</span><span>News</span><span>Investment profiles</span><span>Contact us</span></nav>

<section class="abs hero">
  <div class="hero-photo" role="img" aria-label="Photo of a cheering team of young professionals with raised fists in a bright office"></div>
  <p class="hero-caption">Lorem Ipsum is simply dummy text of the printing and typesetting industry. Lorem Ipsum has been the industry's standard dummy text ever since the 1500s, when an unknown printer took a galley of type and scrambled it to make a type specimen book.</p>
</section>

<a class="abs funding" href="#">
  <h2>FUNDING</h2>
  <h3>APPLICATION</h3>
  <svg class="go" width="30" height="30" viewBox="0 0 30 30"><circle cx="15" cy="15" r="14" fill="#fff"/><polygon points="12,8 20,15 12,22" fill="#222"/></svg>
</a>

<section class="abs panel profiles">
  <div class="panel-head">Investment Profiles<svg width="14" height="7"><polygon points="0,0 14,0 7,7" fill="#5a9a16"/></svg></div>
  <div class="partner">Calder Brook &amp; Lowe</div>
  <div class="partner" style="color:#555;font-weight:400">The Bank of Westmere</div>
  <div class="partner" style="color:#1f4a3c">Pell &amp; Ardent</div>
  <a class="view-all" style="top:205px" href="#">VIEW ALL</a>
</section>

<div class="abs rule"></div>

<section class="abs panel about">
  <h4>About Our Firm</h4>
  <ul>
    <li>Partner profiles - We will include photographs and bios about each of the partners in our firm.</li>
    <li>Invest with Bright Harbor - This will include information how to invest with our fund</li>
    <li>our process - About our process for evaluating, funding and helping build successful businesses - This will include a narrative about the target companies, how we work, the type of deals we are interested in, our expectations, etc</li>
  </ul>
</section>

<section class="abs panel news">
  <div class="panel-head">Latest News<svg width="14" height="7"><polygon points="0,0 14,0 7,7" fill="#5a9a16"/></svg></div>
  <ul class="news-list">
    <li><span class="date">01/15/14</span><br>Lorem Ipsum is simply dummy text</li>
    <li><span class="date">01/15/14</span><br>Lorem Ipsum is simply dummy text</li>
    <li><span class="date">01/15/14</span><br>Lorem Ipsum is simply dummy text</li>
  </ul>
  <a class="view-all" style="top:171px" href="#">VIEW ALL</a>
</section>

<section class="abs panel growing">
  <h4>Growing Businesses</h4>
  <p>Lorem Ipsum is simply dummy text of the printing and typesetting industry. Lorem Ipsum has been the industry's standard dummy text ever since the 1500s, when an unknown printer took a galley of type and scrambled it to make a type specimen book.</p>
</section>

<section class="abs panel quote">
  <p>Lorem Ipsum is simply dummy text of the printing and typesetting industry. Lorem Ipsum has been the industry's standard dummy text ever since the 1500s, when an unknown printer took a galley of type and scrambled it to make a type specimen book..............</p>
</section>

<svg class="abs" style="left:250px;top:853px" width="194" height="18" viewBox="0 0 194 18"><polygon points="0,8 97,0 194,8 194,18 0,18" fill="#5a9a16"/></svg>
<footer class="abs footer"><p>© Copyright Bright Harbor Capital 2014 - All rights reserved.</p></footer>
</body>
</html>
```